Business card and stationary for eco-aware technology company
Verdalux: Green-minded Scrap Recovery
Business card and stationary for eco-aware technology company - Chemicals
Creative Brief
Professional
Tam Brendow
Managing Director
7-3, 2nd Floor, Pelham Court, Quarry Road, 10450 Georgetown, Penang, Malaysia
+604-8XXXXXX
+6011-5274 XXXX
xxx@verdalux.example
http://www.verdalux.example
YYYYYYY-K
Hello, My name is Tam Brendow, and I am MD of Verdalux. I would like a letterhead and a business card for myself. Verdalux is a Malaysia-based startup with a focus on developing technology for urban mining ( http://scrapharvest.example/ ). Verdalux's name is legally Verdalux Sdn. Bhd., but maybe the shorter form, 'Verdalux' looks better on a business card. Perhaps the "Sdn. Bhd." could be hidden in there somewhere. Up to you! For the business card, the following info should be used: Tam Brendow Managing Director MChem, Ph.D (Chemistry) The back side of the business card can be blank, or it can be very simply decorated. I am on Malaysian time (GMT +8) so please forgive me if my feedback appears delayed. Thanks & good luck, - Tam
Empty is fine. Very simple decoration if you want - maybe just the company logo in the center.
tbrendow tbrendow
Hey, Sorry for the slow feedback. I've just got back to the office. Firstly, I am happy to review the business card designs on this site. However, the stationary designs are too big to preview and quorbasketch's site makes it too slow for me to look at the designs. So, would you designers be able to host the images on a web server, or put them in a .zip file? Private message me the URL and I'll download them and use an image viewer to see them offline. Sorry for the extra work - blame QS's crap design. Ok, now for some feedback: 1) The dark 'Eco' green does not look nice on the card. Please use only a little bit! 2) Lighter greens are nice. Like the colour of the 3 leaves. 3) No transparent cards, please. 4) The back of the card should have a very simple design. Maybe just the 3 leaves on a white background, with no text? 5) I love the designs with the big leaf (#191). It's clever. I also love the designs with the circuit pattern (#212, #213, #214). That's clever too. Private message me if you want more feedback or ideas. I'll try to reply fast. Thanks, - Tam

```html
<!DOCTYPE html>
<html lang="en">
<head>
<meta charset="utf-8">
<title>Verdalux Business Card</title>
<link rel="stylesheet" href="https://fonts.googleapis.com/css2?family=Montserrat:wght@700;800&family=Open+Sans:wght@400;600;700&display=swap">
<style>
  :root {
    --bg: #e9ebe6;
    --deep-green: #1f6b2a;
    --mid-green: #3f9a2c;
    --leaf-green: #8cc63f;
    --light-green: #b9dc6a;
    --swoosh-grey: #8a8f88;
    --ink: #3a3f3a;
    --white: #ffffff;
  }
  * { margin: 0; padding: 0; box-sizing: border-box; }
  html, body { width: 1200px; height: 901px; overflow: hidden; }
  body {
    background: var(--bg);
    font-family: "Open Sans", sans-serif;
    position: relative;
  }
  .card {
    position: absolute;
    width: 600px;
    height: 343px;
    border-radius: 14px;
    overflow: hidden;
    box-shadow: 0 6px 18px rgba(0,0,0,0.18);
  }
  /* Back of card */
  .card-back {
    left: 500px; top: 60px;
    background: radial-gradient(circle at 30% 35%, #2f8a32 0%, var(--deep-green) 55%, #17561f 100%);
  }
  .back-brand {
    position: absolute;
    right: 40px; bottom: 70px;
    display: flex; align-items: center; gap: 12px;
  }
  .back-brand .mark-dot {
    width: 34px; height: 34px; border-radius: 50%;
    background: var(--leaf-green);
  }
  .back-brand .name {
    font-family: "Montserrat", sans-serif;
    font-weight: 800;
    font-size: 46px;
    color: var(--white);
    letter-spacing: -1px;
  }
  .back-tagline {
    position: absolute; right: 42px; bottom: 52px;
    font-size: 11px; font-weight: 700; letter-spacing: 1.6px;
    color: var(--light-green); text-transform: uppercase;
  }
  .back-url {
    position: absolute; right: 42px; bottom: 30px;
    font-size: 12px; letter-spacing: 2px; color: var(--white);
  }
  /* Front of card */
  .card-front {
    left: 100px; top: 460px;
    background: var(--white);
  }
  .front-brand {
    position: absolute; left: 34px; top: 30px;
    display: flex; align-items: center; gap: 10px;
  }
  .front-brand .mark-dot {
    width: 30px; height: 30px; border-radius: 50%;
    background: var(--leaf-green);
  }
  .front-brand .name {
    font-family: "Montserrat", sans-serif;
    font-weight: 800;
    font-size: 36px;
    color: var(--mid-green);
    letter-spacing: -1px;
  }
  .front-tagline {
    position: absolute; left: 76px; top: 74px;
    font-size: 9px; font-weight: 700; letter-spacing: 1.4px;
    color: var(--deep-green); text-transform: uppercase;
  }
  .person { position: absolute; left: 34px; top: 104px; }
  .person .full-name { font-size: 19px; font-weight: 600; color: var(--deep-green); }
  .person .degree { font-size: 12px; color: var(--ink); margin-top: 2px; }
  .person .role { font-size: 12px; color: var(--ink); margin-top: 1px; }
  .wave { position: absolute; left: 0; bottom: 0; width: 600px; height: 200px; }
  .license {
    position: absolute; left: 22px; bottom: 48px;
    font-size: 10px; color: var(--white);
    transform: rotate(-8deg); transform-origin: left bottom;
  }
  .contact {
    position: absolute; right: 24px; bottom: 66px;
    list-style: none; text-align: right;
    font-size: 11.5px; color: var(--white); line-height: 17px;
  }
  .contact li { display: flex; justify-content: flex-end; align-items: center; gap: 7px; }
  .contact svg { width: 11px; height: 11px; flex: none; }
  .address {
    position: absolute; right: 24px; bottom: 16px;
    text-align: right; font-size: 11px; line-height: 15px; color: var(--white);
  }
</style>
</head>
<body>

<section class="card card-back" aria-label="Back of business card">
  <div class="back-brand"><span class="mark-dot"></span><span class="name">Verdalux</span></div>
  <div class="back-tagline">Green-minded Scrap Recovery</div>
  <div class="back-url">www.verdalux.example</div>
</section>

<section class="card card-front" aria-label="Front of business card">
  <div class="front-brand"><span class="mark-dot"></span><span class="name">Verdalux</span></div>
  <div class="front-tagline">Green-minded Scrap Recovery</div>

  <div class="person">
    <div class="full-name">Tam Brendow</div>
    <div class="degree">MChem, Ph.D (Chemistry)</div>
    <div class="role">Managing Director</div>
  </div>

  <svg class="wave" viewBox="0 0 600 200" preserveAspectRatio="none" aria-hidden="true">
    <defs>
      <linearGradient id="band" x1="0" y1="0" x2="1" y2="1">
        <stop offset="0" stop-color="#a8d24f"/>
        <stop offset="0.5" stop-color="#6cb33a"/>
        <stop offset="1" stop-color="#3f9a2c"/>
      </linearGradient>
    </defs>
    <path d="M0 70 C150 20 300 120 600 30 L600 200 L0 200 Z" fill="url(#band)"/>
    <path d="M0 62 C160 8 320 112 600 20" fill="none" stroke="#8a8f88" stroke-width="6"/>
    <path d="M0 55 C160 0 320 104 600 10" fill="none" stroke="#c9ccc6" stroke-width="2"/>
  </svg>

  <div class="license">License No. YYYYYYY-K</div>

  <ul class="contact">
    <li>604-8XXXXXX
      <svg viewBox="0 0 12 12"><path d="M3 1 L5 3.5 L4 5 Q5.5 7 7 8 L8.5 7 L11 9 L9.5 11 Q4 10 1 2.5 Z" fill="#fff"/></svg></li>
    <li>6011-5274 XXXX
      <svg viewBox="0 0 12 12"><rect x="3.5" y="0.5" width="5" height="11" rx="1" fill="none" stroke="#fff"/><circle cx="6" cy="9.5" r="0.8" fill="#fff"/></svg></li>
    <li>604-8000 412
      <svg viewBox="0 0 12 12"><rect x="1" y="4" width="10" height="7" rx="1" fill="#fff"/><rect x="3" y="1" width="6" height="4" fill="none" stroke="#fff"/></svg></li>
    <li>xxx@verdalux.example
      <svg viewBox="0 0 12 12"><rect x="0.5" y="2.5" width="11" height="7" fill="none" stroke="#fff"/><path d="M0.5 2.5 L6 7 L11.5 2.5" fill="none" stroke="#fff"/></svg></li>
    <li>www.verdalux.example
      <svg viewBox="0 0 12 12"><circle cx="6" cy="6" r="5" fill="none" stroke="#fff"/><ellipse cx="6" cy="6" rx="2" ry="5" fill="none" stroke="#fff"/><path d="M1 6 H11" stroke="#fff"/></svg></li>
  </ul>

  <div class="address">7-3, 2nd Floor, Pelham Court, Quarry Road,<br>10450 Georgetown, Penang, Malaysia</div>
</section>

</body>
</html>
```